Instagram ad design required

For an IT system house, we need an ad design for a job recruiting campaign on Instagram. A great engaging advertisement is required that encourages potential applicants to click on the ad. The recruiting funnel already exists, only an Instagram ad image should be designed. Follow-up orders for further campaigns as well as Facebook and LinkedIn are possible.
The design of the IT system house Varnholt serves as a design inspiration: www.varnholt.com
The customer should be perceived as a great, modern employer. The target group are young IT technicians who want to work in a cool and modern company. For example, the topic could be IT Super Hero wanted with corresponding graphic content.
Target Market(s)
IT system technician
Industry/Entity Type
Informatik
Other font styles liked:
- PT Sans
Look and feel
Each slider illustrates characteristics of the customer's brand and the style your logo design should communicate.

```html
<!DOCTYPE html>
<html lang="en">
<head>
<meta charset="utf-8">
<title>Varnholt – We Are Hiring</title>
<link href="https://fonts.googleapis.com/css2?family=Oswald:wght@400;500;600;700&family=Montserrat:wght@400;500;600;700&display=swap" rel="stylesheet">
<style>
  :root {
    --green-dark: #008a4d;
    --green-light: #7dc242;
    --cream: #f2f5e6;
    --white: #ffffff;
    --ink: #3a3a3a;
    --photo-a: #e9ecef;
    --photo-b: #c9d1d6;
    --photo-c: #9cc94a;
  }
  html, body {
    margin: 0;
    padding: 0;
    width: 1200px;
    height: 1200px;
    overflow: hidden;
    background: var(--white);
  }
  .ad { display: block; width: 1200px; height: 1200px; }
  .display { font-family: "Oswald", sans-serif; }
  .body-text { font-family: "Montserrat", sans-serif; }
  .fill-dark { fill: var(--green-dark); }
  .fill-light { fill: var(--green-light); }
  .fill-cream { fill: var(--cream); }
  .fill-white { fill: var(--white); }
  .fill-ink { fill: var(--ink); }
</style>
</head>
<body>
<svg class="ad" viewBox="0 0 1200 1200" xmlns="http://www.w3.org/2000/svg">
  <defs>
    <linearGradient id="photoTone" x1="0" y1="0" x2="1" y2="1">
      <stop offset="0" stop-color="var(--photo-a)"/>
      <stop offset="0.55" stop-color="var(--photo-b)"/>
      <stop offset="1" stop-color="var(--photo-c)"/>
    </linearGradient>
  </defs>

  <!-- base -->
  <rect class="fill-dark" x="0" y="0" width="1200" height="1200"/>

  <!-- top accent strip -->
  <rect class="fill-light" x="0" y="0" width="1200" height="26"/>

  <!-- hero photo area -->
  <rect class="hero-photo" x="0" y="26" width="1200" height="531" fill="url(#photoTone)"
        role="img" aria-label="Photo of a smiling young IT technician with glasses in a white shirt, seated in a green armchair in a bright modern office"/>

  <!-- slanted brand band -->
  <polygon class="brand-band fill-light" points="85,26 374,26 291,557 0,557 0,420"/>

  <!-- company name -->
  <g class="company-name">
    <text class="display fill-white" x="70" y="384" font-size="48" font-weight="600"
          letter-spacing="1">VARNHOLT</text>
  </g>

  <!-- headline -->
  <g class="headline">
    <rect class="fill-white" x="72" y="622" width="203" height="81"/>
    <text class="display fill-dark" x="84" y="690" font-size="68" font-weight="500"
          textLength="180" lengthAdjust="spacingAndGlyphs">WE ARE</text>
    <text class="display fill-white" x="66" y="878" font-size="205" font-weight="600"
          textLength="470" lengthAdjust="spacingAndGlyphs">HIRING !</text>
    <rect class="fill-white" x="72" y="890" width="463" height="80"/>
    <text class="display" x="92" y="952" font-size="52" font-weight="500"
          textLength="424" lengthAdjust="spacingAndGlyphs"><tspan class="fill-dark">WE WANT </tspan><tspan class="fill-light">IT SUPER HERO</tspan></text>
  </g>

  <!-- contact footer -->
  <g class="contact-footer">
    <rect class="fill-light" x="0" y="1030" width="1200" height="170"/>

    <g class="contact-email">
      <rect class="fill-white" x="83" y="1106" width="46" height="32" rx="2"/>
      <polyline points="83,1108 106,1126 129,1108" fill="none" stroke="var(--green-light)" stroke-width="3"/>
      <text class="body-text fill-white" x="142" y="1113" font-size="17" font-weight="400">EMAIL YOUR RESUME :</text>
      <text class="body-text fill-white" x="142" y="1140" font-size="22" font-weight="600">recruiting@varnholt.com</text>
    </g>

    <g class="contact-phone">
      <path class="fill-white" d="M490 1100 l10 -3 l7 15 l-7 5 q5 11 15 17 l6 -7 l14 8 l-3 10 q-4 5 -12 3 q-26 -9 -34 -36 q-1 -8 4 -12 z"/>
      <text class="body-text fill-white" x="548" y="1113" font-size="17" font-weight="400">CALL US FOR DETAILS :</text>
      <text class="body-text fill-white" x="548" y="1140" font-size="22" font-weight="600">+49 7132 555-0147</text>
    </g>

    <g class="contact-web" fill="none" stroke="var(--white)" stroke-width="3">
      <circle cx="830" cy="1122" r="22"/>
      <ellipse cx="830" cy="1122" rx="10" ry="22"/>
      <line x1="808" y1="1122" x2="852" y2="1122"/>
      <line x1="812" y1="1110" x2="848" y2="1110"/>
      <line x1="812" y1="1134" x2="848" y2="1134"/>
    </g>
    <text class="body-text fill-white" x="864" y="1113" font-size="17" font-weight="400">MORE INFORMATION :</text>
    <text class="body-text fill-white" x="864" y="1140" font-size="22" font-weight="600">https://www.varnholt.com</text>
  </g>

  <!-- position card -->
  <g class="position-card">
    <rect class="fill-cream" x="598" y="500" width="545" height="558"/>
    <rect class="fill-light" x="598" y="500" width="545" height="115"/>
    <polygon class="fill-light" points="852,614 888,614 870,634"/>
    <text class="display fill-white" x="870" y="580" font-size="58" font-weight="500"
          text-anchor="middle" textLength="388" lengthAdjust="spacingAndGlyphs">POSITION AVAILABE</text>

    <polygon class="fill-ink" points="641,672 641,702 657,687"/>
    <text class="display fill-ink" x="670" y="707" font-size="52" font-weight="400"
          textLength="243" lengthAdjust="spacingAndGlyphs">IT TECHNICIAN</text>

    <text class="body-text fill-ink" x="641" y="764" font-size="20" font-weight="700">JOB DESCRIPTION :</text>
    <line x1="641" y1="778" x2="1110" y2="778" stroke="#9a9a9a" stroke-width="1.5" stroke-dasharray="2 3"/>

    <g class="body-text fill-ink" font-size="20">
      <circle cx="647" cy="810" r="4.5"/>
      <text x="660" y="817">Lorem ipsum dolor sit amet, consectetur adip</text>
      <text x="660" y="843">sicing elit, sed do eiusmod tempor.</text>

      <circle cx="647" cy="876" r="4.5"/>
      <text x="660" y="883">Tempor incididunt ut labore et dolore magna</text>
      <text x="660" y="909">aliqua. Ut enim ad minim veniam, quis nostr</text>
      <text x="660" y="935">ud exercitation ullamco laboris nisiut aliq</text>
      <text x="660" y="961">uip ex ea commodo consequat.</text>

      <circle cx="647" cy="987" r="4.5"/>
      <text x="660" y="994">Lorem ipsum dolor sit amet, consectetur adip</text>
      <text x="660" y="1020">sicing elit, sed do eiusmod tempor.</text>
    </g>
  </g>
</svg>
</body>
</html>
```